Christmas social media advert post

I am looking for an eye catching advert for use mainly on social media posts.
The following is the detail of the event.

Christmas special offer-
£10pp,– offer includes –
Half an hour Toboggan track,
Half an hour Slingshot paintballs (20 paintballs pp) and safe target archery (under cover and indoor ranges). Activities all the family from age 4 to grandparents can join in,
Also available – Add on indoor activities including Mini Curling, Bead Blitz, Safe axe throwing, Air juggler – from £3.50pp and age 6plus
Café open for hot food and drinks in the ‘Fireside Frost Lodge and the heated Christmas marquee.

A basic idea I put together for what I feel is the important information is -

Christmas Special offer -
Starts Saturday 20th December.
£10pp – offer includes –
Half an hour Slingshot paintballs (20 paintballs pp) and safe target archery (under cover and indoor ranges). Activities all the family from age 4 to grandparents can join in. Booking is essential - details on how below.
Also available Add on indoor activities - including Mini Curling, Bead Blitz, Safe axe throwing, Air juggler – from £3.50pp and age 6plus.
Ages start from 4 plus.
All activities are great for children and adults so perfect for families as well as friends, parties and get togethers.
Free huge car parks,
Booking is easy-
Just Message from messenger (on this post) or email
martin@hollowbrookleisurepark.co.uk for availability of your preferred date and time.

I would be happy to send the detailed information to enquiries if it meant a better looking advert / post.

Full details are in the picture uploads, feel free to use as much or as little of the information as you feel best.

```html
<!DOCTYPE html>
<html lang="en">
<head>
<meta charset="utf-8">
<title>Christmas Special Offer</title>
<link href="https://fonts.googleapis.com/css2?family=Dancing+Script:wght@700&family=League+Gothic&family=Poppins:ital,wght@0,400;0,600;0,700;0,800;1,400;1,600;1,800;1,900&display=swap" rel="stylesheet">
<style>
  :root {
    --red: #c8141b;
    --red-dark: #8e0d10;
    --green: #0f7a24;
    --green-dark: #0a5a3a;
    --ink: #2f2f2f;
    --ink-soft: #3c3c3c;
    --white: #ffffff;
    --paper: #ffffff;
    --pine: #2f6b2a;
  }
  * { margin: 0; padding: 0; box-sizing: border-box; }
  html, body { width: 1200px; height: 1200px; overflow: hidden; background: var(--paper); }
  body { font-family: "Poppins", sans-serif; color: var(--ink); }
  .poster { position: relative; width: 1200px; height: 1200px; overflow: hidden; background: var(--paper); }
  .abs { position: absolute; }

  .garland { left: 0; top: 0; width: 470px; height: 330px; }

  .archery-photo { left: 730px; top: 680px; width: 470px; height: 520px;
    background: linear-gradient(90deg, rgba(255,255,255,1) 0%, rgba(226,222,214,0.8) 30%, #b9ae9e 70%, #97897a 100%); }
  .archery-fade { left: 730px; top: 680px; width: 470px; height: 520px;
    background: linear-gradient(180deg, rgba(255,255,255,1) 0%, rgba(255,255,255,0) 28%); }

  .hero { left: 0; top: 0; width: 1200px; height: 620px; }

  .title-script { left: 120px; top: 82px; font-family: "Dancing Script", cursive; font-size: 118px; color: var(--red); line-height: 1; }
  .title-main { left: 104px; top: 196px; font-family: "League Gothic", sans-serif; font-size: 190px; color: var(--ink); line-height: 1;
    letter-spacing: -1px; text-shadow: 4px 3px 0 #d9d9d9; transform: scaleX(0.61); transform-origin: left top; white-space: nowrap; }

  .date-band { left: 42px; top: 360px; width: 660px; height: 105px; border-radius: 52px 0 0 52px;
    background: linear-gradient(90deg, var(--green) 0%, var(--green-dark) 100%); border: 3px solid var(--green-dark); }
  .date-starts { left: 92px; top: 368px; color: var(--white); font-style: italic; font-size: 41px; line-height: 38px; }
  .date-day { left: 298px; top: 360px; color: var(--white); font-style: italic; font-weight: 900; font-size: 82px; line-height: 1.15; }
  .date-month { left: 515px; top: 405px; color: var(--white); font-style: italic; font-size: 40px; }

  .offer-list { left: 45px; top: 477px; list-style: none; width: 455px; }
  .offer-list li { position: relative; padding-left: 23px; margin-bottom: 12px; font-size: 24px; line-height: 30px; }
  .offer-list li::before { content: ""; position: absolute; left: 0; top: 11px; width: 12px; height: 12px; border-radius: 50%; background: var(--red); }
  .offer-list strong { font-weight: 700; color: var(--ink); font-size: 25px; letter-spacing: -0.5px; }
  .divider { left: 499px; top: 480px; width: 1px; height: 130px; background: #9a9a9a; }
  .family-note { left: 512px; top: 486px; width: 280px; font-size: 24px; line-height: 30px; color: var(--ink-soft); }

  .booking-band { left: 0; top: 617px; width: 935px; height: 49px;
    background: linear-gradient(90deg, var(--red) 0%, var(--red) 55%, rgba(200,20,27,0.25) 100%); }
  .booking-text { left: 45px; top: 622px; color: var(--white); font-style: italic; font-weight: 600; font-size: 26px; }

  .price-badge { left: 892px; top: 442px; width: 256px; height: 256px; border-radius: 50%; background: var(--white);
    box-shadow: 0 0 0 3px var(--red-dark), 0 0 0 8px var(--white); overflow: hidden; }
  .price-top { position: absolute; left: 0; top: 0; width: 100%; height: 134px; background: linear-gradient(180deg, var(--red-dark), var(--red)); text-align: center; color: var(--white); }
  .price-amount { font-weight: 800; font-size: 52px; line-height: 1; padding-top: 33px; }
  .price-sub { font-size: 25px; margin-top: 8px; }
  .price-bottom { position: absolute; top: 147px; width: 100%; text-align: center; font-size: 22px; line-height: 29px; color: var(--ink); }

  .addon-box { left: 45px; top: 680px; width: 678px; height: 192px; border: 2px solid var(--red); border-radius: 14px; overflow: hidden; background: var(--white); }
  .addon-title { position: absolute; top: 7px; width: 100%; text-align: center; font-size: 26px; color: var(--ink-soft); }
  .addon-list { position: absolute; top: 45px; left: 32px; width: 620px; list-style: none; display: grid; grid-template-columns: 320px 300px; row-gap: 2px; }
  .addon-list li { position: relative; padding-left: 25px; font-size: 27px; font-weight: 600; color: var(--ink); line-height: 35px; }
  .addon-list li::before { content: ""; position: absolute; left: 0; top: 13px; width: 12px; height: 12px; border-radius: 50%; background: var(--red-dark); }
  .addon-price { position: absolute; left: 0; bottom: 0; width: 100%; height: 66px; background: linear-gradient(90deg, var(--green-dark), var(--green)); color: var(--white); font-weight: 700; font-size: 31px; text-align: center; line-height: 62px; }

  .cafe-band { left: 0; top: 884px; width: 820px; height: 76px;
    background: linear-gradient(90deg, var(--red) 0%, var(--red) 60%, rgba(200,20,27,0.2) 100%); }
  .cafe-text { left: 46px; top: 888px; width: 740px; color: var(--white); font-weight: 700; font-size: 25px; line-height: 32px; letter-spacing: -0.5px; white-space: nowrap; }

  .age-badge { left: 792px; top: 860px; width: 124px; height: 124px; border-radius: 50%; background: linear-gradient(135deg, var(--red), var(--red-dark));
    box-shadow: 0 0 0 4px var(--white), 0 2px 6px rgba(0,0,0,0.25); color: var(--white); text-align: center; }
  .age-label { font-size: 26px; padding-top: 22px; line-height: 1; }
  .age-value { font-size: 40px; font-weight: 800; line-height: 1.15; }

  .audience { left: 46px; top: 964px; width: 720px; font-size: 24px; line-height: 30px; color: var(--ink-soft); }

  .contact-band { left: 195px; top: 1035px; width: 1005px; height: 80px; background: linear-gradient(90deg, var(--red-dark), var(--red)); }
  .contact-pill { left: 0; top: 1035px; width: 197px; height: 80px; border-radius: 0 40px 40px 0; background: var(--green-dark);
    box-shadow: 3px 0 0 var(--white); color: var(--white); font-weight: 700; font-size: 26px; line-height: 29px; padding: 12px 0 0 45px; }
  .contact-text { left: 210px; top: 1040px; color: var(--white); font-size: 28px; line-height: 32px; }
  .contact-text strong { font-weight: 700; }
  .contact-divider { left: 940px; top: 1040px; width: 2px; height: 72px; background: rgba(255,255,255,0.7); }
  .parking { left: 968px; top: 1043px; width: 200px; text-align: center; color: var(--white); font-weight: 800; font-size: 30px; line-height: 31px; letter-spacing: -0.5px; }

  .availability { left: 45px; top: 1123px; font-style: italic; font-size: 24px; color: var(--ink-soft); }
</style>
</head>
<body>
<main class="poster">
  <svg class="abs garland" viewBox="0 0 470 330" role="img" aria-label="Evergreen garland with gold stars and baubles">
    <defs>
      <linearGradient id="pineFade" x1="0" y1="0" x2="1" y2="1">
        <stop offset="0" stop-color="#2f6b2a"/>
        <stop offset="0.7" stop-color="#3d7d36"/>
        <stop offset="1" stop-color="#3d7d36" stop-opacity="0"/>
      </linearGradient>
    </defs>
    <path d="M0 0 H465 C430 40 380 70 300 80 C220 90 160 100 120 130 C100 170 90 240 70 330 H0 Z" fill="url(#pineFade)"/>
  </svg>

  <div class="abs archery-photo" role="img" aria-label="Photo of a child practising archery in a covered indoor range"></div>
  <div class="abs archery-fade"></div>

  <svg class="abs hero" viewBox="0 0 1200 620">
    <defs>
      <linearGradient id="ringRed" x1="0" y1="0" x2="1" y2="1">
        <stop offset="0" stop-color="#d4161d"/>
        <stop offset="1" stop-color="#7d0b0e"/>
      </linearGradient>
      <linearGradient id="snowScene" x1="0" y1="0" x2="0" y2="1">
        <stop offset="0" stop-color="#6b5a48"/>
        <stop offset="0.35" stop-color="#c9cfd8"/>
        <stop offset="1" stop-color="#eef1f6"/>
      </linearGradient>
    </defs>
    <path d="M660 0 C590 80 560 200 590 300 C630 440 760 560 900 590 C1010 610 1120 580 1200 530 V0 Z" fill="url(#ringRed)"/>
    <circle cx="935" cy="170" r="332" fill="#ffffff" opacity="0.9"/>
    <circle cx="935" cy="170" r="325" fill="url(#snowScene)" role="img" aria-label="Photo of children sliding down a snowy woodland track on inflatable tubes"/>
  </svg>

  <div class="abs title-script">Christmas</div>
  <div class="abs title-main">SPECIAL OFFER</div>

  <div class="abs date-band"></div>
  <div class="abs date-starts">Starts<br>Saturday</div>
  <div class="abs date-day">20th</div>
  <div class="abs date-month">Dec</div>

  <ul class="abs offer-list">
    <li><strong>Half an hour Slingshot Paintballs</strong><br>(20 paintballs pp)</li>
    <li><strong>Safe Target Archery</strong><br>(under cover and indoor ranges)</li>
  </ul>
  <div class="abs divider"></div>
  <p class="abs family-note">Activities all<br>the family from<br>age 4 to grandparents<br>can join in.</p>

  <div class="abs booking-band"></div>
  <p class="abs booking-text">Booking is essential - details on how below.</p>

  <div class="abs price-badge">
    <div class="price-top">
      <div class="price-amount">£10pp</div>
      <div class="price-sub">offer includes</div>
    </div>
    <div class="price-bottom">Half an hour<br>Toboggan Track</div>
  </div>

  <section class="abs addon-box">
    <p class="addon-title">Also available indoor activities</p>
    <ul class="addon-list">
      <li>Mini Curling</li>
      <li>Safe Axe Throwing</li>
      <li>Bead Blitz</li>
      <li>Air Juggler</li>
    </ul>
    <p class="addon-price">from £3.50pp and age 6plus.</p>
  </section>

  <div class="abs cafe-band"></div>
  <p class="abs cafe-text">Café open for hot food and drinks in the ‘Fireside Frost<br>Lodge and the heated Christmas marquee.</p>

  <div class="abs age-badge">
    <div class="age-label">Age</div>
    <div class="age-value">4+</div>
  </div>

  <p class="abs audience">All activities are great for children and adults so perfect for families as well as friends, parties and get togethers.</p>

  <div class="abs contact-band"></div>
  <div class="abs contact-pill">BOOKING<br>IS EASY</div>
  <p class="abs contact-text">Just Message from messenger (on this post)<br>email: <strong>martin@hollowbrookleisurepark.co.uk</strong></p>
  <div class="abs contact-divider"></div>
  <p class="abs parking">FREE HUGE CAR PARKS</p>

  <p class="abs availability">for availability of your preferred date and time.</p>
</main>
</body>
</html>
```